Dental Design, very professional and noticable

Copperleaf Ridge Dental Surgery is based in Pelican Waters. We are a fast growing dental surgery and are looking for some professional business cards to send to patients.
We would like to see a design that is Vertical and uses the colours Soft Blue, Silver, White and Black. Maybe a full blue side with moto and details on back? Any other ideas or colours that you may think will make the card look unique is fine.
We need all details on the card that are listed above

Target Market(s)

Families, Retired, Other Professionals and Businesses

Industry/Entity Type

Dental

Contact Information for Business Card

Copperleaf Ridge Dental Surgery
Family, Cosmetic, Preventative
Dr. Owen Farrish
Dental Surgeon
BDS (MELB) MDS FRACDS FPDA
phone: (07)54810296
fax: (07)54926170
email: copperleafridgedental@quillpost.net
http://copperleafridgedental.quillpost.net/

Logo Text

Logo styles of interest
Abstract Logo
Requirements
Must have
• Vertical, Vibrant but Professional, Rounded Edges, Logo on front and back of card (different colours on each side)
Nice to have
• One side completely blue (not sure what shade) with logo and moto on bottom
Other side white, with blue or different coloured logo with details in black and silver?
Logo should show half circle with 1 end as arrow symbolizing pelican waters canal also a magnifine glass also half circled with 1 end as arrow. Any other ideas are welcome.
Should not have
• A tooth. A smile. Toothbrush or Toothpaste. Cornered edges.

```html
<!DOCTYPE html>
<html lang="en">
<head>
<meta charset="utf-8">
<title>Copperleaf Ridge Dental Surgery – Business Card</title>
<link rel="stylesheet" href="https://fonts.googleapis.com/css2?family=Arvo:wght@400;700&display=swap">
<style>
  :root {
    --backdrop: #2b2b2b;
    --card-white: #ffffff;
    --card-blue: #44b8e8;
    --ink: #111111;
    --accent-blue: #2a9fd8;
    --rule: #333333;
  }
  * { box-sizing: border-box; margin: 0; padding: 0; }
  html, body { width: 1200px; height: 900px; overflow: hidden; }
  body {
    background: var(--backdrop);
    font-family: "Arvo", Georgia, serif;
    color: var(--ink);
    position: relative;
  }
  .card {
    position: absolute;
    top: 160px;
    width: 330px;
    height: 580px;
    border-radius: 26px;
    text-align: center;
    box-shadow: 0 16px 40px rgba(0,0,0,.55);
  }
  .card--appointment { left: 230px; background: var(--card-white); }
  .card--contact { left: 640px; background: var(--card-blue); }

  .brand { display: flex; flex-direction: column; align-items: center; }
  .brand__dot { width: 56px; height: 56px; border-radius: 50%; margin-bottom: 12px; }
  .brand__name {
    font-weight: 700; font-size: 22px; line-height: 1.05;
    text-transform: uppercase; letter-spacing: .3px;
  }
  .brand__motto { font-size: 15px; margin-top: 4px; }

  .card--appointment .brand { margin-top: 112px; }
  .card--appointment .brand__dot { background: var(--accent-blue); }
  .card--appointment .brand__name { color: var(--accent-blue); font-size: 20px; }

  .slot { margin: 0 auto; width: 220px; }
  .slot__line { border-top: 1.5px solid var(--rule); }
  .slot__label { font-size: 8px; text-transform: uppercase; margin-top: 2px; }
  .slot--date { margin-top: 72px; }
  .slot--time { margin-top: 36px; }
  .notice {
    color: var(--accent-blue); font-size: 12px; line-height: 1.35;
    margin: 72px 26px 0;
  }

  .card--contact .brand { margin-top: 62px; }
  .card--contact .brand__dot { background: var(--ink); }
  .card--contact .brand__name { color: var(--ink); font-size: 24px; }
  .card--contact .brand__motto { font-size: 16px; }

  .dentist { margin-top: 26px; }
  .dentist__name { font-weight: 700; font-size: 22px; text-transform: uppercase; }
  .dentist__role { font-size: 10px; text-transform: uppercase; line-height: 1.25; }

  .details { margin-top: 12px; font-size: 14px; line-height: 1.3; }
  .details__email { font-size: 12.5px; }
  .details__email strong { color: var(--card-white); }
  .address { margin-top: 12px; font-size: 14px; line-height: 1.25; }
  .website { margin-top: 12px; font-weight: 700; font-size: 12.5px; color: var(--card-white); }
  .social { margin-top: 16px; font-size: 13px; line-height: 1.3; }
  .social__square {
    display: inline-block; width: 13px; height: 13px; border-radius: 3px;
    background: var(--ink); vertical-align: -2px; margin-right: 4px;
  }
</style>
</head>
<body>
  <section class="card card--appointment" aria-label="Appointment side">
    <div class="brand">
      <span class="brand__dot"></span>
      <p class="brand__name">Copperleaf Ridge<br>Dental Surgery</p>
      <p class="brand__motto">Family, Cosmetic, Preventative</p>
    </div>
    <div class="slot slot--date">
      <div class="slot__line"></div>
      <p class="slot__label">Date:</p>
    </div>
    <div class="slot slot--time">
      <div class="slot__line"></div>
      <p class="slot__label">Time:</p>
    </div>
    <p class="notice">This time has been specifically allocated to you,<br>if unable to attend please give 24hrs notice.</p>
  </section>

  <section class="card card--contact" aria-label="Contact side">
    <div class="brand">
      <span class="brand__dot"></span>
      <p class="brand__name">Copperleaf Ridge<br>Dental Surgery</p>
      <p class="brand__motto">Family, Cosmetic, Preventative</p>
    </div>
    <div class="dentist">
      <p class="dentist__name">Dr. Owen Farrish</p>
      <p class="dentist__role">Dental Surgeon<br>BDS (Melb) MDS FRACDS FPDA</p>
    </div>
    <div class="details">
      <p>P: (07)54810296 F: (07)54926170</p>
      <p class="details__email"><strong>copperleafridgedental</strong>@quillpost.net</p>
    </div>
    <div class="address">
      <p>Copperleaf Ridge Shopping Village</p>
      <p>Shop 7 / 128 Copperleaf Ridge Blvd</p>
      <p>Copperleaf Ridge, QLD, 4562</p>
    </div>
    <p class="website">www.copperleafridgedental.quillpost.net</p>
    <div class="social">
      <p><span class="social__square"></span>Like Us:</p>
      <p>Copperleaf Ridge Dental Surgery</p>
    </div>
  </section>
</body>
</html>
```